Now Open Poster

We need a banner for our sports supplement and nutritional store, Harbor Nutrition.
We were hoping for some sort of creative word art piece.
I have drawn my own mock up just to give you all a very basic starting point. But you are free to go with whatever you feel will work best.
The primary objective is simply to explain a little about what the company does, and then direct traffic towards the store with an 'Open Arrow' pointing left.
Text words we have chosen are:
Protein
Creatine
Health
Fitness
Sports Science
Nutrition
Energy
Achievement
Amino Acids
Organic
Supplements
Performance
Testosterone Support
Vitamins
Growth
Diet
Happiness
Weight Loss
Strong
Natural
Vitality
Accomplished
Below the word art we want our logo (See attached options)
Then below the logo the phrase "Success Starts Here"
Dimensions of the poster are 140cm x 60cm.
Colours: Blues/Whites/Greys/Blacks (Lots of white space please)
Here are some cool pieces I found that had some interesting elements that I liked (I'd love to see a mash-up of styles with a street art feel to it. Something funky!):
http://www.moodgrove.example/pin/804417263190552871/
http://www.moodgrove.example/pin/615380924471208539/
http://www.moodgrove.example/pin/804417263192736155/
http://www.moodgrove.example/pin/804417263194418620/
http://www.moodgrove.example/pin/937162048856301742/
Thanks for reading, message me if you have any further questions!
- Tobias

```html
<!DOCTYPE html>
<html lang="en">
<head>
<meta charset="utf-8">
<title>Harbor Nutrition – Now Open</title>
<link rel="stylesheet" href="https://fonts.googleapis.com/css2?family=Alfa+Slab+One&family=Pacifico&family=Ubuntu+Condensed&family=Exo:ital,wght@1,800&family=Exo+2:ital,wght@1,200&family=Oswald:wght@300;500&family=Orbitron:wght@900&family=Roboto:wght@400&family=Ultra&family=Montserrat:wght@300;600;700;900&family=Parisienne&family=Antonio:wght@400&family=Playfair+Display:wght@700&family=Raleway:wght@200&family=Lobster&family=Archivo+Black&family=Fondamento:ital@1&family=Yellowtail&display=swap">
<style>
  :root{
    --cream:#FBF9E8;
    --red:#E21E26;
    --green:#3FAE2A;
    --green-dark:#1E7A1A;
    --blue-band:#1172BB;
    --blue-deep:#1B4F8F;
    --blue-royal:#1B5BA6;
    --blue-mid:#4A7FC1;
    --blue-soft:#5C7FB8;
    --blue-bright:#1196D6;
    --blue-sky:#6CC5F0;
    --blue-pale:#B8CCE4;
    --blue-ocean:#1280C4;
    --lavender:#7C7FB8;
    --white:#FFFFFF;
    --badge:#EAF2F7;
  }
  *{margin:0;padding:0;box-sizing:border-box}
  html,body{width:1200px;height:2799px;overflow:hidden;background:var(--cream)}
  .poster{position:relative;width:1200px;height:2799px;background:var(--cream)}
  .open-title{position:absolute;top:66px;left:0;width:1110px;text-align:center;font:130px/1 "Alfa Slab One",serif;color:var(--red);letter-spacing:2px}
  .open-arrow{position:absolute;left:640px;top:100px;width:170px;height:140px}
  .word-line{position:absolute;left:0;right:0;text-align:center;white-space:nowrap;line-height:1}
  .word-line span{display:inline-block}
  .w-protein{font:110px "Pacifico",cursive;color:#1A8AD0}
  .w-creatine{font:92px "Ubuntu Condensed",sans-serif;color:var(--blue-soft)}
  .w-health{font:800 italic 86px "Exo",sans-serif;color:var(--blue-pale);letter-spacing:6px}
  .w-fitness{font:300 92px "Oswald",sans-serif;color:var(--blue-soft);transform:scaleX(.85)}
  .w-sports{font:500 118px "Oswald",sans-serif;color:var(--blue-mid)}
  .w-nutrition{font:200 italic 124px "Exo 2",sans-serif;color:var(--blue-sky);letter-spacing:4px}
  .w-energy{font:900 112px "Orbitron",sans-serif;color:var(--blue-royal);letter-spacing:2px}
  .w-achievement{font:400 120px "Roboto",sans-serif;color:var(--blue-bright);transform:scaleX(.92)}
  .w-amino{font:68px "Ultra",serif;color:var(--blue-deep)}
  .w-organic{font:600 90px "Montserrat",sans-serif;color:var(--blue-ocean);letter-spacing:.42em}
  .w-supplements{font:104px "Parisienne",cursive;color:var(--lavender);letter-spacing:.16em}
  .w-performance{font:400 124px "Antonio",sans-serif;color:var(--blue-mid);letter-spacing:.22em}
  .w-testosterone{font:700 112px "Playfair Display",serif;color:var(--blue-soft);transform:scaleX(.72);letter-spacing:-1px}
  .w-vitamins{font:900 96px "Montserrat",sans-serif;color:var(--blue-royal);transform:scaleX(1.08)}
  .w-growth{font:200 124px "Raleway",sans-serif;color:var(--blue-deep)}
  .w-diet{font:500 124px "Oswald",sans-serif;color:var(--blue-mid)}
  .w-happiness{font:118px "Lobster",cursive;color:#1897D3;letter-spacing:3px}
  .w-weight{font:200 112px "Raleway",sans-serif;color:#2E7ABF}
  .w-strong{font:80px "Archivo Black",sans-serif;color:var(--blue-mid)}
  .w-natural{font:300 92px "Montserrat",sans-serif;color:var(--blue-deep)}
  .w-vitality{font:108px "Ultra",serif;color:#4A87C9}
  .w-accomplished{font:italic 110px "Fondamento",cursive;color:#2066B0}
  .brand-band{position:absolute;left:0;top:2355px;width:1200px;height:201px;background:var(--blue-band)}
  .brand-tagline{position:absolute;left:170px;top:2378px;color:var(--white);font:700 78px/0.95 "Montserrat",sans-serif}
  .brand-tagline .small{display:block;font-size:62px}
  .brand-badge{position:absolute;left:451px;top:2327px;width:254px;height:254px;border-radius:50%;background:var(--badge);border:6px solid var(--blue-band);display:flex;align-items:center;justify-content:center;text-align:center}
  .brand-name{font:700 34px/1.15 "Montserrat",sans-serif;color:var(--blue-band)}
  .tagline-wrap{position:absolute;left:160px;top:2580px;width:820px;height:200px}
  .tagline-swash{position:absolute;left:0;top:0;width:820px;height:200px}
  .tagline-text{position:absolute;left:20px;top:40px;font:96px/1 "Yellowtail",cursive;color:var(--red);transform:rotate(-8deg);transform-origin:left center;white-space:nowrap}
</style>
</head>
<body>
<main class="poster">
  <h1 class="open-title">OPEN</h1>
  <svg class="open-arrow" viewBox="0 0 170 140" aria-hidden="true">
    <path d="M150 10 C170 60 140 95 80 95 L80 122 L18 78 L80 34 L80 62 C120 62 150 45 150 10 Z" fill="var(--green)" stroke="var(--green-dark)" stroke-width="4" stroke-linejoin="round"/>
  </svg>

  <div class="word-line" style="top:270px"><span class="w-protein">Protein,</span> <span class="w-creatine">Creatine,</span></div>
  <div class="word-line" style="top:402px"><span class="w-health">Health,</span> <span class="w-fitness">FITNESS,</span></div>
  <div class="word-line" style="top:500px"><span class="w-sports">Sports Science,</span></div>
  <div class="word-line" style="top:618px"><span class="w-nutrition">Nutrition,</span></div>
  <div class="word-line" style="top:728px"><span class="w-energy">ENERGY,</span></div>
  <div class="word-line" style="top:836px"><span class="w-achievement">Achievement,</span></div>
  <div class="word-line" style="top:946px"><span class="w-amino">Amino Acids,</span></div>
  <div class="word-line" style="top:1022px"><span class="w-organic">Organic,</span></div>
  <div class="word-line" style="top:1132px"><span class="w-supplements">Supplements,</span></div>
  <div class="word-line" style="top:1262px"><span class="w-performance">PERFORMANCE,</span></div>
  <div class="word-line" style="top:1390px"><span class="w-testosterone">Testosterone Support,</span></div>
  <div class="word-line" style="top:1510px"><span class="w-vitamins">VITAMINS,</span></div>
  <div class="word-line" style="top:1618px"><span class="w-growth">Growth,</span> <span class="w-diet">Diet,</span></div>
  <div class="word-line" style="top:1740px"><span class="w-happiness">Happiness,</span></div>
  <div class="word-line" style="top:1858px"><span class="w-weight">Weight Loss,</span></div>
  <div class="word-line" style="top:1968px"><span class="w-strong">Strong,</span> <span class="w-natural">Natural,</span></div>
  <div class="word-line" style="top:2064px"><span class="w-vitality">Vitality,</span></div>
  <div class="word-line" style="top:2172px"><span class="w-accomplished">Accomplished,</span></div>

  <section class="brand-band">
  </section>
  <p class="brand-tagline"><span class="small">I am</span>Harbor</p>
  <div class="brand-badge"><span class="brand-name">Harbor<br>Nutrition</span></div>

  <div class="tagline-wrap">
    <svg class="tagline-swash" viewBox="0 0 820 200" aria-hidden="true">
      <path d="M40 175 C250 165 520 120 790 20 C560 100 300 150 40 175 Z" fill="var(--red)"/>
    </svg>
    <p class="tagline-text">Success Starts Here</p>
  </div>
</main>
</body>
</html>
```